Tourism Marketing needing sleek, clear design for business card & proposal documents.

***Company background***
"Quiet Harbour" is a company specializing in tourism marketing and project management. We do international wholesale, event management as well as ongoing representation of tourism and hospitality companies.

***Target market***
We cater to tourism companies and hotel professionals.

***Task***
We would like to get a single sided business card designed (but will still consider two sided, we are open to any ideas you may have). The layout for this card should be modern and elegant. Currently we do not have a logo, but we would like our business name in a really simple typography for the business card (similar to Merrow Lounge's logo - www.merrowlounge.com.au).We are after a design that is clear, strong enough to be recognised as Quiet Harbour that does not require any fancy design. Another option is a simple play on QH (Quiet Harbour) or simply have Quiet Harbour featured elsewhere on card more as a brand/logo.

Feel free to submit different fonts if you feel you have any other fonts/designs that may be suitable for this card other than sans serifs. Should this project be successful, we will be considering several other projects for business proposal templates and eventually a website design.

The information that needs to go on the card are as follows:

Odette Farrow
Director
Quiet Harbour
Tourism Marketing & Representation
57 Wendlow Terrace
Prahran, Victoria, 3181 Australia
T +61 428306172 E odette@quietharbour.com.au

***Look and feel***
We'd like the business card design to express the following:
Modern, sleek, elegant, simple, discreet, quality, subtle, professional, creative, innovation

In terms of typography, we like something really simple and blocky (similar font to Merrow Lounge's logo - www.merrowlounge.com.au)

***Colour scheme***
Shades of grey and dark teal

***Note***
Although our main target market are professionals, we would like the business card design to be versatile enough to be used outside of the tourism industry and need to appeal to different markets.

I do not have existing logo. Was hoping for a design that may be clear, strong enough not to require one. Other option is a simple play on QH (Quiet Harbour) or simply have Quiet Harbour featured elsewhere on card more as a brand/logo.

Odette Farrow
Director
Quiet Harbour Pty Ltd 
57 Wendlow Terrace
T +61 428306172  E  odette@quietharbour.com.au

Thank you for designs so far. Many have used a mauve colour which matches our company profile. This is not necessary, as that is just a draft and will be completely redesigned, so dont  feel you need to incorporate the mauve.

My colour preferences are for a white or grey background, and I like fonts in dark teals, grey or other sophisticated but modern colours. feel free to submit different fonts if you you have other fonts you thing would be suitable for this card, along with sans serifs. Should this project be successful, we will be considering several others for business proposal templates and eventually website. 

Target Market(s)

International Hospitality Senior Executives, Directors of International Tourism Companies, Directors of Tourism Bodies Internationally, local Tourism

Industry/Entity Type

Hospitality

Requirements
Should not have
• must not have bright garish colour, swirly patterns or anything that dates too much.

```html
<!DOCTYPE html>
<html lang="en">
<head>
<meta charset="utf-8">
<title>Quiet Harbour — Business Card</title>
<link rel="stylesheet" href="https://fonts.googleapis.com/css2?family=Source+Sans+3:wght@400;700&display=swap">
<style>
  :root {
    --canvas: #ffffff;
    --card: #fdfdfd;
    --card-edge: #3a3a3a;
    --card-shadow: rgba(0, 0, 0, 0.45);
    --ink: #1e1e1e;
    --accent: #3d3b9c;
    --accent-soft: #8e8fcf;
  }
  * { margin: 0; padding: 0; box-sizing: border-box; }
  html, body {
    width: 1200px;
    height: 900px;
    overflow: hidden;
    background: var(--canvas);
  }
  .canvas {
    position: relative;
    width: 1200px;
    height: 900px;
  }
  .card {
    position: absolute;
    top: 296px;
    width: 547px;
    height: 313px;
    background: var(--card);
    border: 1px solid var(--card-edge);
    box-shadow: 4px 4px 4px var(--card-shadow);
    text-align: center;
    font-family: "Source Sans 3", sans-serif;
    color: var(--ink);
  }
  .card--front { left: 36px; }
  .card--back { left: 613px; }

  /* Front */
  .brand {
    position: absolute;
    top: 112px;
    left: 0;
    right: 0;
  }
  .brand__name {
    font-weight: 700;
    font-size: 44px;
    line-height: 1;
    color: var(--ink);
  }
  .brand__tagline {
    margin-top: 12px;
    font-weight: 400;
    font-size: 21px;
    color: var(--accent);
  }

  /* Back */
  .contact {
    position: absolute;
    top: 83px;
    left: 0;
    right: 0;
  }
  .contact__name {
    font-weight: 700;
    font-size: 25px;
    line-height: 1;
    text-transform: uppercase;
    letter-spacing: 0.2px;
  }
  .contact__role {
    margin-top: 2px;
    font-size: 18px;
    color: var(--accent);
  }
  .contact__address {
    margin-top: 18px;
    font-size: 16.5px;
    line-height: 21px;
    font-style: normal;
  }
  .contact__company { font-weight: 700; }
  .contact__lines {
    margin-top: 5px;
    font-size: 17px;
    display: flex;
    justify-content: center;
    gap: 22px;
    transform: translateX(-6px);
  }
  .contact__label {
    font-weight: 700;
    color: var(--accent-soft);
    margin-right: 7px;
  }
</style>
</head>
<body>
  <main class="canvas">
    <section class="card card--front" aria-label="Card front">
      <div class="brand">
        <h1 class="brand__name">Quiet Harbour</h1>
        <p class="brand__tagline">Tourism Marketing &amp; Representation</p>
      </div>
    </section>

    <section class="card card--back" aria-label="Card back">
      <div class="contact">
        <h2 class="contact__name">Odette Farrow</h2>
        <p class="contact__role">Director</p>
        <address class="contact__address">
          <span class="contact__company">Quiet Harbour</span> Pty Ltd<br>
          Tourism Marketing &amp; Representation<br>
          57 Wendlow Terrace Prahran,<br>
          Victoria, 3181 Australia
        </address>
        <p class="contact__lines">
          <span><span class="contact__label">T</span>+61 428306172</span>
          <span><span class="contact__label">E</span>odette@quietharbour.com.au</span>
        </p>
      </div>
    </section>
  </main>
</body>
</html>
```